Simple and Approachable Cover for Pet Expo Company Page

Size: 2000 x 430; looking simply for words "Dunmore HR Consulting" and email address "DunmoreHRConsulting@brelvamail.com." This is for a cover photo for a company profile page for the Hollow Oak Expo, where I am a featured speaker on Employee Communications later this month. You can incorporate the attached photo to the left of the banner ad if you wish. The mood I wish to present is approachable, positive and simple.

Target Market(s)

small pet retail business owners

Industry/Entity Type

Pet Shop

Font styles to use
Serif
Sans Serif

Requirements
Must have
• Email address clearly defined/separated. Easy to read.
Nice to have
• I like the picture that I included; subtle pet paw background is also nice
Should not have
• No paid stock images

```html
<!DOCTYPE html>
<html lang="en">
<head>
<meta charset="utf-8">
<title>Dunmore HR Consulting – Cover</title>
<link rel="stylesheet" href="https://fonts.googleapis.com/css2?family=Playfair+Display:wght@900&family=Roboto:wght@400&display=swap">
<style>
  :root {
    --page-bg: #ffffff;
    --banner-yellow: #f5ce55;
    --band-light: #f3c04b;
    --band-dark: #eeac3e;
    --title-navy: #0b2d42;
    --email-ink: #151515;
    --rule-white: #ffffff;
    --photo-grass: #7d8a4a;
    --photo-trees: #4f5e37;
    --photo-warm: #b98a57;
    --dog-orange: #d88a3f;
    --dog-cream: #f1dcc0;
    --hat-yellow: #f0b52c;
  }
  html, body {
    margin: 0;
    padding: 0;
    width: 1200px;
    height: 1200px;
    overflow: hidden;
    background: var(--page-bg);
  }
  .cover {
    position: absolute;
    left: 28px;
    top: 477px;
    width: 1144px;
    height: 246px;
    background: var(--banner-yellow);
    overflow: hidden;
  }
  .cover-art {
    position: absolute;
    inset: 0;
    width: 100%;
    height: 100%;
  }
  .company-name {
    position: absolute;
    left: 370px;
    width: 640px;
    top: 86px;
    margin: 0;
    text-align: center;
    white-space: nowrap;
    font-family: "Playfair Display", Georgia, serif;
    font-weight: 900;
    font-size: 42px;
    line-height: 1;
    letter-spacing: -0.2px;
    color: var(--title-navy);
  }
  .contact-email {
    position: absolute;
    left: 489px;
    top: 145px;
    margin: 0;
    display: flex;
    align-items: center;
    gap: 11px;
    white-space: nowrap;
    font-family: "Roboto", Arial, sans-serif;
    font-size: 18px;
    color: var(--email-ink);
  }
  .contact-email svg {
    width: 30px;
    height: 23px;
    flex: none;
  }
</style>
</head>
<body>
  <section class="cover">
    <svg class="cover-art" viewBox="0 0 1144 246" preserveAspectRatio="none">
      <defs>
        <linearGradient id="teamPhotoTone" x1="0" y1="0" x2="0" y2="1">
          <stop offset="0" stop-color="var(--photo-trees)"/>
          <stop offset="0.45" stop-color="var(--photo-warm)"/>
          <stop offset="1" stop-color="var(--photo-grass)"/>
        </linearGradient>
        <linearGradient id="dogPhotoTone" x1="0" y1="0" x2="0" y2="1">
          <stop offset="0" stop-color="var(--hat-yellow)"/>
          <stop offset="0.4" stop-color="var(--dog-orange)"/>
          <stop offset="1" stop-color="var(--dog-cream)"/>
        </linearGradient>
      </defs>
      <path class="band-light" d="M0 0 H378 Q444 123 378 246 H0 Z" fill="var(--band-light)"/>
      <path class="band-dark" d="M0 0 H347 Q419 123 347 246 H0 Z" fill="var(--band-dark)"/>
      <path class="team-photo" role="img" aria-label="Photo of the consultant couple sitting on grass in a park with their two hound dogs" d="M0 0 H313 Q393 123 313 246 H0 Z" fill="url(#teamPhotoTone)"/>
      <rect class="dog-photo" role="img" aria-label="Photo of a smiling shiba inu wearing a yellow knit hat" x="990" y="0" width="154" height="246" fill="url(#dogPhotoTone)"/>
      <line class="rule-top" x1="503" y1="0" x2="503" y2="89" stroke="var(--rule-white)" stroke-width="1.5"/>
      <polyline class="rule-bottom" points="863,158 920,158 920,246" fill="none" stroke="var(--rule-white)" stroke-width="1.5"/>
    </svg>

    <h1 class="company-name">Dunmore HR Consulting</h1>

    <p class="contact-email">
      <svg viewBox="0 0 30 23" aria-hidden="true">
        <rect x="0.75" y="0.75" width="28.5" height="21.5" fill="none" stroke="var(--email-ink)" stroke-width="1.2"/>
        <polyline points="1,1 15,13 29,1" fill="none" stroke="var(--email-ink)" stroke-width="1.2"/>
        <line x1="1" y1="22" x2="11" y2="10" stroke="var(--email-ink)" stroke-width="1.2"/>
        <line x1="29" y1="22" x2="19" y2="10" stroke="var(--email-ink)" stroke-width="1.2"/>
      </svg>
      <span>DunmoreHRConsulting@brelvamail.com</span>
    </p>
  </section>
</body>
</html>
```